Brochure Design For Beauty Salon

We have an existing brochure for our beauty salon business which has been designed in-house.

We need a designer to refresh the look and feel of the brochure, which is intended for print. The print format will be 210mmx210mm (square, stapled).

We need a design for each and every page of the brochure, including the front and back covers.

We are looking for a fresh modern design, quite close to what we already have, but looking more slick and professional.

The primary colors are white, grey and purple. The final design will communicate luxury, prestige and cleanliness and have a heavy focus on creating the feeling of space within each page.

Target Market(s)

Professional Women, aged 20-45

Industry/Entity Type

Beauty Salon

Font styles to use
Sans Serif
Other font styles liked:
• Helvetica

Requirements
Must have
• The project must be ready for print on square paper 210x210mm

```html
<!DOCTYPE html>
<html lang="en">
<head>
<meta charset="utf-8">
<title>Halden Studio – Treatment Menu</title>
<link href="https://fonts.googleapis.com/css2?family=Raleway:wght@300;400;600&display=swap" rel="stylesheet">
<style>
:root{
  --plum:#5b1636;
  --taupe:#b9ab8f;
  --paper:#ffffff;
  --ink:#4a3a40;
  --muted:#8b7e73;
  --bg:#d9d9d9;
  --frame:rgba(255,255,255,.75);
}
*{box-sizing:border-box;margin:0;padding:0}
html,body{width:1089px;height:1200px;overflow:hidden;background:var(--bg);font-family:"Raleway",Helvetica,Arial,sans-serif;color:var(--ink)}
.canvas{position:relative;width:1089px;height:1200px}
.spread{position:absolute;width:420px;height:210px;display:flex;box-shadow:0 2px 6px rgba(0,0,0,.18)}
.page{position:relative;width:210px;height:210px;overflow:hidden;background:var(--paper)}
.page.taupe{background:var(--taupe)}
.page.plum{background:var(--plum)}
.frame{position:absolute;inset:8px;border:1px solid var(--frame)}
.topband{position:absolute;left:0;right:0;top:0;height:6px;background:var(--plum)}
.band{position:absolute;left:0;right:0;background:var(--taupe)}
.band.plum{background:var(--plum)}
.photo{position:absolute;background:linear-gradient(135deg,#efe2d6,#c9b39d)}
.photo.cool{background:linear-gradient(135deg,#e4ecef,#b9c7cc)}
.photo.warm{background:linear-gradient(135deg,#f1d2b6,#c98f67)}
.photo.room{background:linear-gradient(135deg,#f2eee5,#d8c9b0 60%,#b9a07d)}
.label{position:absolute;left:0;right:0;bottom:14px;text-align:center;font-weight:300;font-size:15px;color:#fff;letter-spacing:.5px}
.h{font-weight:300;font-size:15px;color:var(--plum);letter-spacing:.4px}
.h4{font-weight:600;font-size:6px;color:var(--plum);margin-top:4px}
.t{font-size:4.6px;line-height:1.45;color:var(--ink)}
.row{display:flex;justify-content:space-between;align-items:center;font-size:4.8px;line-height:1.5;gap:4px}
.tag{display:inline-block;background:var(--plum);color:#fff;font-size:4.4px;padding:1px 4px;margin:1px 0;white-space:nowrap}
.tags{display:flex;flex-direction:column;align-items:flex-end}
.box{position:absolute}
.muted{color:var(--muted)}
.cover-name{position:absolute;left:0;right:0;top:24px;text-align:center;color:#fff;font-weight:400;font-size:15px;letter-spacing:.6px}
.cover-sub{position:absolute;left:0;right:0;bottom:20px;text-align:center;color:#fff;font-weight:300;font-size:13px}
.back-text{position:absolute;left:0;right:0;top:48px;text-align:center;color:#fff;font-weight:300}
.back-text .name{font-weight:400;font-size:15px;letter-spacing:.6px;margin-bottom:14px}
.back-text p{font-size:8.5px;line-height:1.7}
</style>
</head>
<body>
<main class="canvas">

  <section class="spread" style="left:72px;top:30px">
    <div class="page plum">
      <div class="frame"></div>
      <div class="cover-name">Halden Studio</div>
      <div class="photo room" style="left:20px;top:56px;width:170px;height:96px" role="img" aria-label="Photo of the bright salon reception with a curved white seat and cushions"></div>
      <div class="cover-sub">Treatment Menu</div>
    </div>
    <div class="page taupe">
      <div class="frame"></div>
      <div class="back-text">
        <div class="name">Halden Studio</div>
        <p>020 7946 0123</p>
        <p>48 Elmwood Road</p>
        <p>Hartfield Green · N9 4QT</p>
        <p style="margin-top:6px">www.haldenstudio.co.uk</p>
      </div>
    </div>
  </section>

  <section class="spread" style="left:597px;top:30px">
    <div class="page">
      <div class="topband"></div>
      <div class="box" style="left:14px;right:14px;top:16px">
        <div class="h4">Signature Facials</div>
        <p class="t">Deep cleansing and hydrating, our signature facials are tailored to your skin.</p>
        <div class="row"><span>Micro Signature Facial</span><span class="tag">£35 | 30 mins</span></div>
        <p class="t muted">A focused treatment for visible results.</p>
        <div class="row"><span>Halden Signature Facial</span><span class="tag">£55 | 60 mins</span></div>
        <p class="t muted">A bespoke facial for every skin stage.</p>
        <div class="row"><span>Luxury Signature Facial</span><span class="tag">£85 | 90 mins</span></div>
        <p class="t muted">Includes massage and soothing touch therapy.</p>
      </div>
      <div class="band" style="top:140px;height:70px"></div>
      <div class="box" style="left:14px;right:14px;top:146px">
        <div class="h4">Eye Lift</div>
        <div class="row"><span>Eyelift Micro Facial</span><span class="tag">£35 | 30 mins</span></div>
        <div class="row"><span>Eyelift Add-on</span><span class="tag">£15 | 15 mins</span></div>
        <p class="t">A gentle treatment to brighten and firm the eye area.</p>
      </div>
    </div>
    <div class="page">
      <div class="box" style="left:14px;right:14px;top:14px">
        <div class="h4">Teenage Facials</div>
        <p class="t">Gentle care for young skin.</p>
        <div class="row"><span>Fresh Start Facial</span><span class="tag">£30 | 30 mins</span></div>
        <div class="row"><span>Fresh Start Signature Facial</span><span class="tag">£45 | 60 mins</span></div>
        <div class="row"><span>Fresh Start Luxury Facial</span><span class="tag">£70 | 90 mins</span></div>
      </div>
      <div class="photo cool" style="left:0;right:0;top:104px;height:92px" role="img" aria-label="Photo of a client receiving a facial treatment"></div>
      <div class="band plum" style="bottom:0;height:14px"></div>
    </div>
  </section>

  <section class="spread" style="left:72px;top:260px">
    <div class="page taupe">
      <div class="frame"></div>
      <div class="photo" style="left:16px;top:16px;width:178px;height:146px" role="img" aria-label="Photo of a woman with a facial mask applied by brush"></div>
      <div class="label">Dermaclear Facials</div>
    </div>
    <div class="page">
      <div class="photo" style="left:0;right:0;top:0;height:58px" role="img" aria-label="Photo of a relaxed woman with a white towel"></div>
      <div class="box" style="left:14px;right:14px;top:66px">
        <div class="h">Dermaclear Facials</div>
        <p class="t" style="margin-top:4px">The results you are going to see with a Dermaclear skin treatment are unlike anything else. We cleanse, exfoliate and massage with care.</p>
        <div class="row" style="justify-content:flex-end"><span class="tag">£10 | 10 mins</span></div>
        <div class="h4">Skin Solver</div>
        <p class="t">Receive your skin regimen under the guidance of a therapist and learn how to use the products at home.</p>
      </div>
      <div class="band plum" style="bottom:0;height:8px"></div>
    </div>
  </section>

  <section class="spread" style="left:597px;top:260px">
    <div class="page">
      <div class="topband"></div>
      <div class="box" style="left:14px;right:14px;top:16px">
        <div class="row"><span class="h4" style="margin:0">Contemporary Massage</span><span class="tag">£45 | 45 mins</span></div>
        <p class="t">Deep cleansing and ultra hydrating, our signature treatments are made for you.</p>
        <div class="row"><span>Indian Head Massage</span><span class="tag">£60 | 60 mins</span></div>
        <div class="row"><span>Mud Massage</span><span class="tag">£60 | 60 mins</span></div>
        <div class="row"><span>Thermal Compress Massage</span><span></span></div>
      </div>
      <div class="photo warm" style="left:14px;right:14px;top:94px;height:40px" role="img" aria-label="Photo of a hot stone massage"></div>
      <span class="tag box" style="right:16px;top:124px">Coming Soon</span>
      <div class="band" style="top:140px;height:70px"></div>
      <div class="box" style="left:14px;right:14px;top:148px">
        <div class="row"><span>Warm Shell Massage</span><span class="tag">£35 | 30 mins</span></div>
        <div class="row"><span>Warm Shell Back Massage</span><span class="tag">£65 | 60 mins</span></div>
        <div class="row"><span>Warm Shell Full Body Massage</span><span></span></div>
      </div>
    </div>
    <div class="page taupe">
      <div class="frame"></div>
      <div class="photo cool" style="left:16px;top:16px;width:178px;height:146px" role="img" aria-label="Photo of a woman in white sitting on a chair holding a sun hat"></div>
      <div class="label">Spa Body</div>
    </div>
  </section>

  <section class="spread" style="left:72px;top:490px">
    <div class="page taupe">
      <div class="frame"></div>
      <div class="photo warm" style="left:16px;top:16px;width:178px;height:146px" role="img" aria-label="Photo of a couple receiving back massages"></div>
      <div class="label">Massage</div>
    </div>
    <div class="page">
      <div class="topband"></div>
      <div class="box" style="left:14px;right:14px;top:18px">
        <div class="h" style="text-align:center">Massage</div>
        <p class="t" style="margin-top:4px">You need a massage that combines the best techniques from around the world. Choose your ideal massage and it will be tailored to your needs.</p>
        <div class="tags" style="margin-top:6px">
          <span class="tag">30 mins | £32.00</span>
          <span class="tag">60 mins | £49.00</span>
          <span class="tag">90 mins | £72.00</span>
        </div>
        <div class="h4">Signature Massage</div>
        <p class="t">Back, Neck and Shoulders</p>
        <p class="t">Full Body</p>
        <p class="t">Luxury Massage</p>
      </div>
      <div class="band plum" style="bottom:0;height:8px"></div>
    </div>
  </section>

  <section class="spread" style="left:597px;top:490px">
    <div class="page taupe">
      <div class="frame"></div>
      <div class="photo warm" style="left:16px;top:16px;width:178px;height:146px" role="img" aria-label="Photo of warm wax applied to a leg with a spatula"></div>
      <div class="label">Waxing</div>
    </div>
    <div class="page">
      <div class="topband"></div>
      <div class="box" style="left:14px;right:14px;top:18px">
        <div class="h" style="text-align:center">Waxing</div>
        <p class="t" style="margin-top:4px">Our expert therapists are trained to the highest standards, providing professional and hygienic waxing treatments.</p>
        <div style="display:flex;gap:10px;margin-top:6px">
          <div style="flex:1">
            <div class="h4">Leg waxing</div>
            <div class="row"><span>Half leg</span><span class="tag">£18.00</span></div>
            <div class="row"><span>Upper legs</span><span class="tag">£22.00</span></div>
            <div class="row"><span>¾ legs</span><span class="tag">£24.00</span></div>
            <div class="row"><span>Full legs</span><span class="tag">£29.00</span></div>
          </div>
          <div style="flex:1">
            <div class="h4">Bikini waxing</div>
            <div class="row"><span>Bikini</span><span class="tag">£16.00</span></div>
            <div class="row"><span>High bikini</span><span class="tag">£22.00</span></div>
            <div class="row"><span>Brazilian</span><span class="tag">£29.00</span></div>
            <div class="row"><span>Hollywood</span><span class="tag">£36.00</span></div>
            <div class="row"><span>½ buttocks</span><span class="tag">£9.00</span></div>
            <div class="row"><span>Full buttocks</span><span class="tag">£18.00</span></div>
          </div>
        </div>
      </div>
    </div>
  </section>

  <section class="spread" style="left:72px;top:720px">
    <div class="page">
      <div class="topband"></div>
      <div class="box" style="left:14px;right:14px;top:18px">
        <div class="h" style="text-align:center">Spa Body</div>
        <p class="t" style="margin-top:4px">Through the benefits of heat and the power of touch, experience a results-oriented body treatment.</p>
        <div class="row"><span class="h4">Body Exfoliation</span><span class="tag">£40 | 45 mins</span></div>
        <p class="t muted">An exfoliating treatment that polishes skin.</p>
        <div class="row"><span class="h4">Body Wrap</span><span class="tag">£45 | 45 mins</span></div>
        <p class="t muted">An intense wrap to nourish skin.</p>
      </div>
      <div class="band" style="top:150px;height:60px"></div>
      <div class="box" style="left:14px;right:14px;top:158px">
        <div class="row"><span class="h4" style="margin:0">Dermaclear Back Pure</span><span class="tag">£36 | 30 mins</span></div>
        <p class="t">Deep cleanse for the back, including extraction.</p>
      </div>
    </div>
    <div class="page">
      <div class="topband"></div>
      <div class="box" style="left:14px;right:14px;top:18px">
        <div class="h" style="text-align:center">Sun Glow Tan</div>
        <p class="t" style="margin-top:4px">Sun Glow Tan works with your natural skin pigment to produce a natural golden glow. Please exfoliate before your tan.</p>
        <div class="row"><span>Full body scrub and tan</span><span class="tag">£49 | 60 mins</span></div>
        <div class="row"><span>Full body tan</span><span class="tag">£32 | 30 mins</span></div>
        <div class="row"><span>Full leg scrub and tan</span><span class="tag">£29 | 30 mins</span></div>
        <div class="row"><span>Full leg tan</span><span class="tag">£18 | 15 mins</span></div>
      </div>
    </div>
  </section>

  <section class="spread" style="left:597px;top:720px">
    <div class="page">
      <div class="photo" style="left:0;right:0;top:0;height:54px" role="img" aria-label="Close-up photo of a closed eye with long lashes"></div>
      <div class="topband" style="top:54px"></div>
      <div class="box" style="left:14px;right:14px;top:66px">
        <div class="h4">Threading</div>
        <div class="row"><span>Lip, chin, neck or sideburns</span><span class="tag">£6.00</span></div>
        <div class="row"><span>Half face</span><span class="tag">£20.00</span></div>
        <div class="row"><span>Full face including eyebrows</span><span class="tag">£26.00</span></div>
        <div class="h4">Combos</div>
        <div class="row"><span>Lip and eyebrows</span><span class="tag">£12 / £14</span></div>
        <div class="row"><span>Chin and neck</span><span class="tag">£10 / £12</span></div>
        <div class="h4">Waxing</div>
        <div class="row"><span>Lip, chin, neck or sideburns</span><span class="tag">£7.00</span></div>
        <div class="row"><span>Full face including eyebrows</span><span class="tag">£30.00</span></div>
        <div class="row"><span>Nostrils</span><span class="tag">£7.00</span></div>
      </div>
    </div>
    <div class="page taupe">
      <div class="frame"></div>
      <div class="photo" style="left:16px;top:16px;width:178px;height:146px" role="img" aria-label="Portrait photo of a woman applying mascara"></div>
      <div class="label">Brows and Lashes</div>
    </div>
  </section>

  <section class="spread" style="left:72px;top:950px">
    <div class="page">
      <div class="photo" style="left:120px;top:0;width:60px;height:40px" role="img" aria-label="Photo of a woman in a towel"></div>
      <div class="box" style="left:14px;right:14px;top:44px">
        <div class="h4">Arm waxing</div>
        <div class="row"><span>Underarm</span><span class="tag">£10.00</span></div>
        <div class="row"><span>½ arm</span><span class="tag">£14.00</span></div>
        <div class="row"><span>Full arm</span><span class="tag">£21.00</span></div>
      </div>
      <div class="band" style="top:96px;height:22px"></div>
      <div class="box" style="left:14px;right:14px;top:101px">
        <div class="row"><span>Full arm and underarm</span><span class="tag">£25.00</span></div>
      </div>
      <div class="box" style="left:14px;right:14px;top:124px">
        <div class="h4">Body Waxing</div>
        <div class="row"><span>Navel line</span><span class="tag">£6.00</span></div>
        <div class="row"><span>½ stomach</span><span class="tag">£9.00</span></div>
        <div class="row"><span>Full stomach, chest and breasts</span><span class="tag">£14.00</span></div>
        <div class="row"><span>Lower back</span><span class="tag">£9.00</span></div>
        <div class="row"><span>Full back</span><span class="tag">£23.00</span></div>
      </div>
    </div>
    <div class="page">
      <div class="topband"></div>
      <div class="box" style="left:14px;right:14px;top:16px">
        <div class="h4">Waxing Combo Packages</div>
        <div class="row"><span>Lower leg &amp; Bikini</span><span class="tag">£30.00</span></div>
        <div class="row"><span>Lower leg &amp; Brazilian</span><span class="tag">£40.00</span></div>
        <div class="row"><span>Lower leg &amp; Hollywood</span><span class="tag">£46.00</span></div>
        <div class="row"><span>Full leg &amp; Bikini</span><span class="tag">£40.00</span></div>
        <div class="row"><span>Full leg &amp; Brazilian</span><span class="tag">£50.00</span></div>
        <div class="row"><span>Full leg &amp; Hollywood</span><span class="tag">£56.00</span></div>
        <div class="row"><span>Add underarm to any package</span><span class="tag">£5.00</span></div>
        <div class="h4">Full Body Waxing Packages</div>
        <div class="row"><span>Full body, ½ stomach, lower back</span><span class="tag">£70.00</span></div>
        <div class="row"><span>Basic full body, full arm, underarm</span><span class="tag">£75.00</span></div>
        <div class="row"><span>Ultimate full body, full back</span><span class="tag">£90.00</span></div>
        <div class="row"><span>Full face and eyebrow shape</span><span class="tag">£115.00</span></div>
      </div>
      <div class="band plum" style="bottom:0;height:8px"></div>
    </div>
  </section>

</main>
</body>
</html>
```